Create an art-deco/vintage poster for restaurant

We need a poster to promote our new 'high tea' offering - Marlowe presents Miss Thornbury's Splendid Old Fashioned Tea Rooms.
The poster will sit inside a chrome frame of an old art deco movie theatre. We'd like the poster to have an art-deco, vintage feel, while still looking fresh and eye catching to passers by. The size should be total 128cm tall by 72 cm wide. There's also a chrome band that sits 11-15cm down the poster that will be covered (see photo).
Wording should include along the lines of:
Indulge in a selection of savouries and sweets, decadent desserts, fine teas, coffee or bubbles with art-deco charm and fabulous views.
Served weekends from midday.

We'd also like a matching A4 menu border template.

Our logo, frame and inspiration images attached.

About the restaurant.
Set in the historic Regent picture theatre building, MARLOWE Restaurant and Bar at Katoomba combines playful art-deco charm with hearty food, friendly service and spectacular Blue Mountains views.
Located on main street Katoomba, enter the historic 1936 Regent picture theatre foyer and make your way past the ticket booth and up the stairs. The restaurant inhabits the dress circle of the old theatre, and offers a decor of quirky retro finds and spectacular mountain views over Leura and the Jamison Valley.

Meals are prepared in the old projection room, and cocktails and retro tunes are served in the former refreshment lounge, now a cosy bar complete with roaring fireplace. The art deco architecture is complemented by an eclectic collection of furnishings and artwork. The style of service is casual and friendly.

www.marlowedining.com.au

Target Market(s)

Tourists visiting the area, and locals who'd like to experience our new offering.

Industry/Entity Type

Restaurant

Font styles to use
Serif
Decorative
Script

Requirements
Must have
• Must be eye-catching to passers by, and suit the art deco style of the building. To be able to be printed and used in frame.
Nice to have
• Colourful.

```html
<!DOCTYPE html>
<html lang="en">
<head>
<meta charset="utf-8">
<title>Miss Thornbury's Splendid Old Fashioned Tea Rooms</title>
<link rel="stylesheet" href="https://fonts.googleapis.com/css2?family=Andika:wght@700&family=Berkshire+Swash&family=Bubblegum+Sans&family=Cinzel:wght@600;700&family=Comfortaa:wght@700&family=Mali:wght@700&family=Uncial+Antiqua&family=Yanone+Kaffeesatz:wght@500&display=swap">
<style>
  :root {
    --paper-green: #c9d3a3;
    --paper-cream: #e3d7b0;
    --paper-peach: #e2b98f;
    --paper-mint: #b9d3b6;
    --ink: #141414;
    --sketch-green: #7f9c57;
    --tile-red: #8f2b2f;
    --tile-edge: #f1e3dc;
    --rust: #b4521f;
    --teal: #2b9a83;
    --pink: #d24a6d;
    --leaf: #3d8a69;
    --blue: #3b6aa8;
    --plum: #5d2a68;
    --olive: #5a4a1a;
    --magenta: #a23c82;
  }
  * { margin: 0; padding: 0; box-sizing: border-box; }
  html, body { width: 857px; height: 1200px; overflow: hidden; }
  body { background: var(--paper-cream); }

  .poster {
    position: relative;
    width: 857px;
    height: 1200px;
    overflow: hidden;
    background:
      radial-gradient(ellipse 360px 300px at 620px 180px, rgba(150,190,110,.55), transparent 70%),
      radial-gradient(ellipse 300px 260px at 120px 560px, rgba(232,180,140,.45), transparent 70%),
      radial-gradient(ellipse 380px 280px at 700px 1050px, rgba(226,185,143,.6), transparent 70%),
      radial-gradient(ellipse 340px 260px at 180px 1000px, rgba(185,211,182,.7), transparent 70%),
      radial-gradient(ellipse 300px 240px at 450px 760px, rgba(170,205,190,.5), transparent 70%),
      linear-gradient(160deg, var(--paper-cream), var(--paper-green) 45%, var(--paper-mint) 70%, var(--paper-peach));
  }

  .sketch-portrait {
    position: absolute;
    left: 420px; top: 17px;
    width: 437px; height: 463px;
    border-radius: 45% 40% 30% 35%;
    background: radial-gradient(ellipse at 55% 45%, rgba(110,150,70,.45), rgba(127,156,87,.2) 60%, transparent 78%);
  }

  .cup-ring {
    position: absolute;
    left: -20px; top: 885px;
    width: 500px; height: 330px;
  }

  .brand {
    position: absolute;
    left: 26px; top: 40px;
    width: 402px;
    text-align: center;
    font-family: "Cinzel", serif;
    font-weight: 700;
    font-size: 44px;
    letter-spacing: 4px;
    color: var(--ink);
  }
  .presents {
    position: absolute;
    left: 26px; top: 137px;
    width: 402px;
    text-align: center;
    font-family: "Cinzel", serif;
    font-weight: 600;
    font-size: 17px;
    letter-spacing: 3px;
    color: var(--ink);
  }

  .headline { position: absolute; left: 0; top: 0; width: 857px; height: 520px; }
  .headline__miss { font-family: "Berkshire Swash", serif; fill: #fbfaf4; }
  .headline__name { font-family: "Berkshire Swash", serif; fill: var(--ink); }
  .headline__splendid { font-family: "Uncial Antiqua", serif; fill: var(--rust); }
  .headline__oldfashioned { font-family: "Comfortaa", sans-serif; font-weight: 700; fill: var(--teal); }

  .big-tile {
    position: absolute;
    display: flex; align-items: center; justify-content: center;
    background: var(--tile-red);
    border: 2px solid var(--tile-edge);
    font-family: "Bubblegum Sans", sans-serif;
    color: var(--tile-red);
    -webkit-text-stroke: 3px var(--tile-edge);
    paint-order: stroke fill;
    line-height: 1;
  }

  .offer { position: absolute; white-space: nowrap; line-height: 1; }
  .offer--intro { left: 34px; top: 688px; font-family: "Comfortaa", sans-serif; font-weight: 700; font-size: 31px; color: var(--ink); letter-spacing: -.5px; }
  .offer--savouries { left: 118px; top: 727px; font-family: "Mali", sans-serif; font-weight: 700; font-size: 29px; color: var(--pink); }
  .offer--teas { left: 262px; top: 766px; font-family: "Andika", sans-serif; font-weight: 700; font-size: 31px; color: var(--leaf); }
  .offer--bubbles { left: 30px; top: 808px; font-family: "Yanone Kaffeesatz", sans-serif; font-weight: 500; font-size: 40px; color: var(--blue); }
  .offer--desserts { left: 538px; top: 714px; font-family: "Yanone Kaffeesatz", sans-serif; font-weight: 500; font-size: 40px; color: var(--plum); }
  .offer--coffee { left: 594px; top: 764px; font-family: "Comfortaa", sans-serif; font-weight: 700; font-size: 31px; color: var(--olive); }
  .offer--views { left: 619px; top: 808px; font-family: "Yanone Kaffeesatz", sans-serif; font-weight: 500; font-size: 40px; color: var(--magenta); }

  .waiter-figure {
    position: absolute;
    left: 420px; top: 778px;
    width: 162px; height: 80px;
    border-radius: 50%;
    background: radial-gradient(ellipse at 60% 45%, #4d7a6b, #1e1e1e 70%);
  }

  .served {
    position: absolute;
    left: 34px; top: 874px;
    width: 802px;
    display: flex; justify-content: space-between; align-items: center;
  }
  .served__word { display: flex; gap: 1px; }
  .small-tile {
    display: inline-flex; align-items: center; justify-content: center;
    min-width: 24px; height: 30px; padding: 0 3px;
    background: var(--tile-edge);
    border: 1px solid var(--tile-red);
    font-family: "Bubblegum Sans", sans-serif;
    font-size: 28px; line-height: 1;
    color: var(--tile-red);
  }
  .small-tile--dark { background: var(--tile-red); color: var(--tile-edge); }
  .small-tile:nth-child(3n+1) { transform: rotate(-5deg) translateY(2px); }
  .small-tile:nth-child(3n+2) { transform: rotate(4deg) translateY(-3px); }
  .small-tile:nth-child(3n) { transform: rotate(-2deg) translateY(1px); }
</style>
</head>
<body>
<main class="poster">
  <div class="sketch-portrait" role="img" aria-label="Vintage pen sketch of a lady sipping from a teacup, in soft green ink"></div>

  <svg class="cup-ring" viewBox="0 0 500 330" role="img" aria-label="Faint coffee cup ring stain">
    <ellipse cx="250" cy="200" rx="225" ry="160" fill="none" stroke="#8fa36a" stroke-width="14" opacity=".35"/>
  </svg>

  <div class="brand">MARLOWE</div>
  <div class="presents">PRESENTS</div>

  <svg class="headline" viewBox="0 0 857 520" aria-label="Miss Thornbury's Splendid Old Fashioned Tea Rooms">
    <text class="headline__miss" x="26" y="228" font-size="74" textLength="255" lengthAdjust="spacingAndGlyphs">Miss</text>
    <text class="headline__name" x="26" y="338" font-size="118" textLength="402" lengthAdjust="spacingAndGlyphs">Thornbury's</text>
    <text class="headline__splendid" x="56" y="412" font-size="64" textLength="407" lengthAdjust="spacingAndGlyphs">SPLENDID</text>
    <text class="headline__oldfashioned" x="30" y="495" font-size="88" textLength="544" lengthAdjust="spacingAndGlyphs">old fashioned</text>
  </svg>

  <div class="big-tile" style="left:39px;top:531px;width:51px;height:107px;font-size:80px;transform:rotate(-2deg)">t</div>
  <div class="big-tile" style="left:111px;top:497px;width:60px;height:137px;font-size:88px;transform:rotate(-8deg)">e</div>
  <div class="big-tile" style="left:197px;top:549px;width:86px;height:124px;font-size:96px;transform:rotate(-4deg)">a</div>
  <div class="big-tile" style="left:360px;top:506px;width:60px;height:128px;font-size:96px;transform:rotate(3deg)">r</div>
  <div class="big-tile" style="left:429px;top:583px;width:60px;height:81px;font-size:70px;transform:rotate(2deg)">o</div>
  <div class="big-tile" style="left:506px;top:489px;width:107px;height:175px;font-size:140px;transform:rotate(-2deg)">O</div>
  <div class="big-tile" style="left:626px;top:549px;width:120px;height:119px;font-size:96px;transform:rotate(3deg)">m</div>
  <div class="big-tile" style="left:754px;top:523px;width:56px;height:124px;font-size:88px;transform:rotate(-6deg)">s</div>

  <p class="offer offer--intro">Indulge in a selection of</p>
  <p class="offer offer--savouries">savouries and sweets</p>
  <p class="offer offer--teas">fine teas</p>
  <p class="offer offer--bubbles">bubbles with art-deco charm</p>
  <p class="offer offer--desserts">decadent desserts</p>
  <p class="offer offer--coffee">coffee</p>
  <p class="offer offer--views">+ fabulous views</p>

  <div class="waiter-figure" role="img" aria-label="Small illustrated waiter character carrying a silver serving dome"></div>

  <div class="served" aria-label="served weekends from midday.">
    <span class="served__word"><span class="small-tile small-tile--dark">s</span><span class="small-tile">e</span><span class="small-tile">r</span><span class="small-tile">v</span><span class="small-tile">e</span><span class="small-tile">d</span></span>
    <span class="served__word"><span class="small-tile">w</span><span class="small-tile">e</span><span class="small-tile small-tile--dark">e</span><span class="small-tile">k</span><span class="small-tile">e</span><span class="small-tile">n</span><span class="small-tile">d</span><span class="small-tile">s</span></span>
    <span class="served__word"><span class="small-tile small-tile--dark">f</span><span class="small-tile">r</span><span class="small-tile">o</span><span class="small-tile">m</span></span>
    <span class="served__word"><span class="small-tile">m</span><span class="small-tile">i</span><span class="small-tile">d</span><span class="small-tile">d</span><span class="small-tile small-tile--dark">a</span><span class="small-tile">y</span><span class="small-tile small-tile--dark">.</span></span>
  </div>
</main>
</body>
</html>
```